Northlake Imaging Partners
Professional
DMS, RDCS
418 Pellwick Row
Irvine, CA 92606
tvasquell@northlakeimagingpartners.com
www.northlakeimagingpartners.com
Providing high quality ultrasound imaging service in the convenience of the Physician's office.
Increase in quality patient care.
Full body ultrasound 7 days a week
High qulity equipment
Professional staff
Quick turnearound
Your Diagnostic Imaging Specialist
Logo file for NIP stationary

```html
<!DOCTYPE html>
<html lang="en">
<head>
<meta charset="utf-8">
<title>Northlake Imaging Partners – Business Card</title>
<link href="https://fonts.googleapis.com/css2?family=Source+Sans+3:wght@400;600;700&display=swap" rel="stylesheet">
<style>
  :root {
    --backdrop: #e9e9ec;
    --card-white: #ffffff;
    --brand-purple: #9a4f9f;
    --brand-purple-dark: #7e3c84;
    --brand-ink: #5a5a5f;
    --text-light: #ffffff;
    --divider-light: rgba(255,255,255,0.55);
  }
  * { margin: 0; padding: 0; box-sizing: border-box; }
  html, body {
    width: 1200px; height: 780px; overflow: hidden;
    background: var(--backdrop);
    font-family: "Source Sans 3", "Myriad Pro", Arial, sans-serif;
  }
  .canvas {
    position: relative; width: 1200px; height: 780px;
  }
  .business-card {
    position: absolute; left: 110px; top: 110px;
    width: 980px; height: 560px;
    background: var(--card-white);
    border-radius: 34px;
    overflow: hidden;
    box-shadow: 0 10px 30px rgba(0,0,0,0.18);
  }
  .brand-block {
    position: absolute; left: 0; right: 0; top: 60px;
    display: flex; flex-direction: column; align-items: center;
  }
  .brand-mark {
    width: 150px; height: 150px; border-radius: 50%;
    background: var(--brand-purple);
    opacity: 0.9;
  }
  .brand-name {
    margin-top: 22px;
    color: var(--brand-purple);
    font-weight: 700;
    font-size: 40px;
    letter-spacing: 1px;
    text-transform: uppercase;
  }
  .band-rule {
    position: absolute; left: 0; right: 0; top: 322px;
    height: 4px; background: var(--brand-purple);
  }
  .contact-band {
    position: absolute; left: 0; right: 0; top: 334px; bottom: 0;
    background: var(--brand-purple);
    color: var(--text-light);
    display: flex;
  }
  .identity {
    width: 455px; padding: 44px 30px 0 0;
    text-align: right;
  }
  .identity .company {
    font-weight: 700; font-size: 27px; line-height: 1.15;
  }
  .identity .credentials {
    font-weight: 600; font-size: 22px; margin-top: 2px;
  }
  .identity .address {
    font-size: 20px; line-height: 1.35; margin-top: 20px;
  }
  .band-divider {
    width: 2px; margin: 34px 0 40px;
    background: var(--divider-light);
  }
  .contact-list {
    list-style: none; padding: 36px 0 0 28px;
  }
  .contact-list li {
    display: flex; align-items: center; gap: 14px;
    font-size: 20px; line-height: 1; height: 38px;
  }
  .contact-icon {
    width: 22px; height: 22px; flex: none;
  }
</style>
</head>
<body>
<div class="canvas">
  <div class="business-card">
    <div class="brand-block">
      <div class="brand-mark"></div>
      <div class="brand-name">Northlake Imaging Partners</div>
    </div>

    <div class="band-rule"></div>

    <div class="contact-band">
      <div class="identity">
        <div class="company">Northlake Imaging Partners</div>
        <div class="credentials">DMS, RDCS</div>
        <div class="address">418 Pellwick Row<br>Irvine, CA 92606</div>
      </div>
      <div class="band-divider"></div>
      <ul class="contact-list">
        <li>
          <svg class="contact-icon" viewBox="0 0 24 24" aria-hidden="true">
            <path fill="#fff" d="M6.6 10.8a15 15 0 0 0 6.6 6.6l2.2-2.2c.3-.3.7-.4 1-.2 1.1.4 2.3.6 3.6.6.6 0 1 .4 1 1V20c0 .6-.4 1-1 1A17 17 0 0 1 3 4c0-.6.4-1 1-1h3.5c.6 0 1 .4 1 1 0 1.3.2 2.5.6 3.6.1.3 0 .7-.2 1z"/>
          </svg>
          949-555-0142
        </li>
        <li>
          <svg class="contact-icon" viewBox="0 0 24 24" aria-hidden="true">
            <path fill="#fff" d="M7 3h10v5H7zM4 9h16a2 2 0 0 1 2 2v6h-4v4H6v-4H2v-6a2 2 0 0 1 2-2zm4 7v3h8v-3z"/>
          </svg>
          949-555-0187
        </li>
        <li>
          <svg class="contact-icon" viewBox="0 0 24 24" aria-hidden="true">
            <circle cx="12" cy="12" r="11" fill="#fff"/>
            <circle cx="12" cy="12" r="3.6" fill="none" stroke="#9a4f9f" stroke-width="2"/>
            <path d="M15.6 9v4.2c0 1.6 2.6 1.6 2.6-1.2A6.2 6.2 0 1 0 15 17.4" fill="none" stroke="#9a4f9f" stroke-width="2"/>
          </svg>
          tvasquell@northlakeimagingpartners.com
        </li>
        <li>
          <svg class="contact-icon" viewBox="0 0 24 24" aria-hidden="true">
            <circle cx="12" cy="12" r="11" fill="#fff"/>
            <g fill="none" stroke="#9a4f9f" stroke-width="1.5">
              <circle cx="12" cy="12" r="7.5"/>
              <ellipse cx="12" cy="12" rx="3.2" ry="7.5"/>
              <path d="M4.5 12h15M6 8h12M6 16h12"/>
            </g>
          </svg>
          www.northlakeimagingpartners.com
        </li>
      </ul>
    </div>
  </div>
</div>
</body>
</html>
```